Dr. Marissa Tevlin Medical/Chiropractic Business Card

Dr. Tevlin is a chiropractor and will require a business card that she uses every single day to book appointments on the back side of the card. Currently the office name goes by Dr. Marissa Tevlin. The chiropractic profession is based on the diagnosis and manipulative treatment of misalignments of the joints, especially those of the spinal column, which are held to cause other disorders by affecting the nerves, muscles, and organs. Dr. Marissa Tevlin is looking for a contemporary and minimalistic design.

Industry/Entity Type

Medical

Contact Information for Business Card

Name: Dr. Marissa Tevlin; Address: 748 Harcastle Rd South, London, ON N5R 2K7; Phone Number: 519.274.6193; Fax: 519.281.5046; email: marissa.tevlin@quorvamail.com

Requirements
Must have
• ability to write multiple appointments date/time on the back of card

```html
<!DOCTYPE html>
<html lang="en">
<head>
<meta charset="utf-8">
<title>Dr. Marissa Tevlin – Business Card</title>
<link rel="stylesheet" href="https://fonts.googleapis.com/css2?family=Tinos:ital@0;1&family=Arimo:wght@400&display=swap">
<style>
  :root {
    --navy: #0d4f72;
    --navy-deep: #0b2d40;
    --paper: #f7f7f7;
    --paper-edge: #e9e9e9;
    --ink: #3a3a3a;
    --rule: #2e2e2e;
    --backdrop: #d9d9d9;
  }
  * { margin: 0; padding: 0; box-sizing: border-box; }
  html, body { width: 1200px; height: 864px; overflow: hidden; background: var(--backdrop); }
  .canvas { position: relative; width: 1200px; height: 864px; }

  .card {
    position: absolute;
    left: 285px;
    width: 630px;
    height: 360px;
    background: linear-gradient(135deg, var(--paper) 0%, var(--paper-edge) 100%);
    overflow: hidden;
  }
  .card--front { top: 48px; }
  .card--back { top: 456px; }

  /* Front */
  .name-band {
    position: absolute;
    left: 120px; top: 0;
    width: 400px; height: 104px;
    background: var(--navy);
    color: #fff;
    padding: 16px 0 0 24px;
  }
  .name-band__name {
    font-family: "Tinos", "Times New Roman", serif;
    font-weight: 400;
    font-size: 38px;
    line-height: 1.1;
    letter-spacing: 0.5px;
    white-space: nowrap;
  }
  .name-band__title {
    font-family: "Tinos", "Times New Roman", serif;
    font-style: italic;
    font-size: 24px;
    line-height: 1.2;
    color: var(--navy-deep);
    margin-top: 2px;
  }
  .address {
    position: absolute;
    left: 120px; top: 118px;
    font-family: "Arimo", Arial, sans-serif;
    font-style: normal;
    font-size: 17px;
    line-height: 1.3;
    color: var(--ink);
  }
  .contacts {
    position: absolute;
    right: 112px; top: 184px;
    list-style: none;
    font-family: "Arimo", Arial, sans-serif;
    font-size: 18px;
    line-height: 1.35;
    color: var(--ink);
  }
  .contacts li { display: flex; align-items: center; gap: 6px; white-space: nowrap; }
  .contacts svg { width: 14px; height: 14px; fill: var(--navy); flex: none; }
  .corner-block {
    position: absolute;
    right: 0; bottom: 0;
    width: 96px; height: 98px;
    background: var(--navy);
  }

  /* Back */
  .appointments {
    position: absolute;
    inset: 0;
    padding: 26px 60px 0 60px;
    font-family: "Tinos", "Times New Roman", serif;
    color: var(--navy);
  }
  .appointments__title {
    font-size: 42px;
    font-weight: 400;
    line-height: 1.15;
    text-align: center;
    margin-bottom: 14px;
  }
  .date-row {
    display: flex;
    align-items: flex-end;
    gap: 14px;
    height: 40px;
    font-size: 22px;
    letter-spacing: 1px;
  }
  .date-row__line {
    flex: 1;
    border-bottom: 2px solid var(--rule);
    margin-bottom: 6px;
  }
  .appointments__note {
    font-size: 18px;
    line-height: 1.2;
    text-align: center;
    margin-top: 18px;
  }
</style>
</head>
<body>
<main class="canvas">

  <section class="card card--front" aria-label="Business card front">
    <div class="name-band">
      <h1 class="name-band__name">Dr. Marissa Tevlin</h1>
      <p class="name-band__title">chiropractor</p>
    </div>
    <address class="address">
      748 Harcastle Rd South, London<br>ON N5R 2K7
    </address>
    <ul class="contacts">
      <li>
        <svg viewBox="0 0 14 14" aria-label="phone"><path d="M4 1h6a1 1 0 0 1 1 1v10a1 1 0 0 1-1 1H4a1 1 0 0 1-1-1V2a1 1 0 0 1 1-1zm0.8 1.5v8.5h4.4V2.5z"/></svg>
        519.274.6193
      </li>
      <li>
        <svg viewBox="0 0 14 14" aria-label="fax"><path d="M3 1h6l2 2v3h1.5a1 1 0 0 1 1 1v5a1 1 0 0 1-1 1h-11a1 1 0 0 1-1-1V7a1 1 0 0 1 1-1H3zM4 2.2V6h6V3.4L8.6 2.2zM3 8.5v1.2h8V8.5z"/></svg>
        519.281.5046
      </li>
      <li>
        <svg viewBox="0 0 14 14" aria-label="email"><path d="M1 3h12v8H1zm1.3 1.2v0.3L7 7.8l4.7-3.3v-0.3zM2.3 5.9v3.9h9.4V5.9L7 9.2z"/></svg>
        marissa.tevlin@quorvamail.com
      </li>
    </ul>
    <div class="corner-block"></div>
  </section>

  <section class="card card--back" aria-label="Business card back">
    <div class="appointments">
      <h2 class="appointments__title">Appointments</h2>
      <div class="date-row"><span>DATE</span><span class="date-row__line"></span></div>
      <div class="date-row"><span>DATE</span><span class="date-row__line"></span></div>
      <div class="date-row"><span>DATE</span><span class="date-row__line"></span></div>
      <div class="date-row"><span>DATE</span><span class="date-row__line"></span></div>
      <p class="appointments__note">If you are unable to make your appointment , please give 24 hours notice.</p>
    </div>
  </section>

</main>
</body>
</html>
```